ROVN branded stationary template

We need associated stationary to accompany our new logo.

The stationary design will be used on business cards, presentation slides and document templates so needs to be provided in an EPS format so that we can adapt it. The design MUST BE ADAPTABLE.

The logo colour is #4a4195 or RGB 85/68/141. Associated colours that can be used in this stationary should compliment this colour. Other colour choices - the preference would be dark and light purples, blues, black and greys. Done how you see fit.

We want the stationary to compliment the overall design of the logo, so clean sharp lines are what we are looking for. It doesn't need to be overly intricate in design - something simple that compliments the look and feel of the logo is what we want. More focused on lines and shapes around the stationary, not any additional logos or pictures.

UK housing providers

Business

Sans Serif

• Clean sharp appearance, nothing overly elaborate.

```html
<!DOCTYPE html>
<html lang="en">
<head>
<meta charset="utf-8">
<title>ROVN Business Card</title>
<link href="https://fonts.googleapis.com/css2?family=Arimo:wght@400;700&display=swap" rel="stylesheet">
<style>
  :root {
    --brand: #4a4195;
    --purple: #6a60ae;
    --purple-deep: #5a519f;
    --paper: #ffffff;
    --paper-shade: #e4e4e8;
    --backdrop: #d9d9dd;
    --ink-light: #ffffff;
  }
  * { box-sizing: border-box; margin: 0; padding: 0; }
  html, body {
    width: 1200px; height: 950px; overflow: hidden;
    background: var(--backdrop);
    font-family: "Arimo", Arial, sans-serif;
  }
  .sheet {
    width: 1200px; height: 950px;
    display: flex; flex-direction: column; align-items: center; justify-content: center;
    gap: 60px;
  }
  .card {
    position: relative; width: 700px; height: 400px;
    background: var(--paper);
    box-shadow: 0 10px 30px rgba(0,0,0,.18);
    overflow: hidden;
  }
  /* Back of card */
  .card-back {
    background: linear-gradient(120deg, var(--paper) 0%, var(--paper) 45%, var(--paper-shade) 100%);
    display: flex; align-items: center; justify-content: center;
  }
  .brand-lockup { display: flex; align-items: center; gap: 22px; }
  .brand-square { width: 46px; height: 46px; background: var(--brand); }
  .brand-name {
    font-weight: 700; font-size: 78px; letter-spacing: 3px; color: var(--brand); line-height: 1;
  }
  /* Front of card */
  .card-front .split { position: absolute; inset: 0; width: 100%; height: 100%; }
  .contact {
    position: absolute; left: 38px; top: 30px; color: var(--ink-light);
  }
  .contact-name { font-weight: 700; font-size: 23px; }
  .contact-title { font-size: 16px; margin-top: 4px; }
  .contact-address { font-size: 16px; line-height: 1.3; margin-top: 38px; }
  .contact-lines { list-style: none; margin-top: 18px; }
  .contact-lines li {
    display: flex; align-items: center; gap: 12px; font-size: 16px; line-height: 1.5;
  }
  .contact-lines svg { width: 15px; height: 15px; fill: var(--ink-light); flex: none; }
  .front-name {
    position: absolute; right: 44px; top: 60%; transform: translateY(-50%);
    font-weight: 700; font-size: 62px; letter-spacing: 2px; color: var(--purple-deep); line-height: 1;
    white-space: nowrap;
  }
</style>
</head>
<body>
<main class="sheet">

  <section class="card card-back" aria-label="Card back">
    <div class="brand-lockup">
      <span class="brand-square"></span>
      <span class="brand-name">ROVN</span>
    </div>
  </section>

  <section class="card card-front" aria-label="Card front">
    <svg class="split" viewBox="0 0 700 400" preserveAspectRatio="none" aria-hidden="true">
      <polygon points="0,0 470,0 340,400 0,400" fill="var(--purple)"/>
      <line x1="452" y1="0" x2="322" y2="400" stroke="var(--paper)" stroke-width="2"/>
    </svg>

    <div class="contact">
      <p class="contact-name">Mara Linden</p>
      <p class="contact-title">President</p>
      <p class="contact-address">412 Ashgrove<br>Lane, Milbrook<br>HX 4PT</p>
      <ul class="contact-lines">
        <li><svg viewBox="0 0 16 16"><path d="M3 1h3l1 4-2 1c1 2 3 4 5 5l1-2 4 1v3c0 1-1 2-2 2C7 15 1 9 1 3c0-1 1-2 2-2z"/></svg>555 0142 7731</li>
        <li><svg viewBox="0 0 16 16"><path d="M4 0h8a1 1 0 0 1 1 1v14a1 1 0 0 1-1 1H4a1 1 0 0 1-1-1V1a1 1 0 0 1 1-1zm1 2v10h6V2zm3 11a1 1 0 1 0 0 2 1 1 0 0 0 0-2z"/></svg>555 0198 2264</li>
        <li><svg viewBox="0 0 16 16"><path d="M4 1h8v4H4zM1 6h14v6h-3v3H4v-3H1zm4 4v4h6v-4z"/></svg>555 0175 4408</li>
        <li><svg viewBox="0 0 16 16"><path d="M1 3h14v10H1zm1 1v1l6 4 6-4V4z"/></svg>mara@rovn-homes.uk</li>
        <li><svg viewBox="0 0 16 16"><path d="M8 0a8 8 0 1 0 0 16A8 8 0 0 0 8 0zm0 2c.8 1 1.4 2.6 1.6 5H6.4C6.6 4.6 7.2 3 8 2zM2.1 9h2.3c.1 1.9.5 3.5 1.2 4.6A6 6 0 0 1 2.1 9zm0-2a6 6 0 0 1 3.5-4.6C4.9 3.5 4.5 5.1 4.4 7zm4.3 2h3.2c-.2 2.4-.8 4-1.6 5-.8-1-1.4-2.6-1.6-5zm4 4.6c.7-1.1 1.1-2.7 1.2-4.6h2.3a6 6 0 0 1-3.5 4.6zM11.6 7c-.1-1.9-.5-3.5-1.2-4.6A6 6 0 0 1 13.9 7z"/></svg>www.rovn-homes.uk</li>
      </ul>
    </div>

    <span class="front-name">ROVN</span>
  </section>

</main>
</body>
</html>
```